KLT Website Homepage Redesign

My website needs a homepage redesign and banner photos updates for Discovery and SEO Services pages. We sell Search Engine Optimization services. We use Search Engine Optimization techniques to help our clients rank high in search engines like Zorvix. It is an intense competition to consistently rank above other businesses. The problem is there is no easy way to show what the benefits of Search Engine Optimization services look like in an emotional way. I want to use an image from sailboat racing to dramatize that our clients win at Search Engine Optimization marketing.
The following products are desired:
1. Desktop version homepage redesign with a banner that clearly shows we sell Search Engine Optimization services using sailboat racing as a metaphor.
2. Mobile version homepage redesign with a banner that clearly shows we sell Search Engine Optimization services using sailboat racing as a metaphor.
2. New banner photo for the Discovery Page
3. New banner photo for the SEO page
The design must be responsive and show well on desktops, laptops, tablets and mobile phones. The current footer style must be kept. A third service called SEO must be added.
the website URL is www.velmorbix.com
Target Market(s)
Business to Business
Industry/Entity Type
Digital Marketing
Coding
Coded - Design and coding required
Number of Pages Required
1 page
Colors
Designer to choose colors to be used in the design.
Look and feel
Each slider illustrates characteristics of the customer's brand and the style your logo design should communicate.

```html
<!DOCTYPE html>
<html lang="en">
<head>
<meta charset="utf-8">
<title>Velmorbix Applications — Homepage</title>
<link rel="stylesheet" href="https://fonts.googleapis.com/css2?family=Montserrat:wght@300;400;500;600;700;800&display=swap">
<style>
:root{
  --blue:#4a7cc9;
  --blue-dark:#2f5ea8;
  --navy:#0f2340;
  --yellow:#f6c624;
  --orange:#f39c3c;
  --ink:#222;
  --text:#444;
  --pale:#eef2fa;
  --grey-num:#d9d9d9;
  --white:#fff;
  --black:#060606;
}
*{box-sizing:border-box;margin:0;padding:0}
html,body{width:1200px;height:3777px;overflow:hidden}
body{font-family:"Montserrat",sans-serif;color:var(--text);background:var(--white);position:relative}
.abs{position:absolute}

/* header */
.header{left:0;top:0;width:1200px;height:60px;background:var(--blue)}
.header-logo{left:0;top:0;width:395px;height:60px;background:var(--white);clip-path:polygon(0 0,370px 0,395px 60px,0 60px)}
.brand{left:145px;top:8px;color:var(--blue);font-size:22px;font-weight:500;line-height:1.1}
.brand small{display:block;font-size:15px;font-weight:400}
.nav{left:418px;top:0;height:60px;display:flex;align-items:center;gap:41px}
.nav a{color:var(--white);font-size:14px;font-weight:600;text-decoration:none;position:relative}
.nav a.active{color:var(--yellow)}
.nav a.active::after{content:"";position:absolute;left:0;right:0;bottom:-21px;height:3px;background:var(--yellow)}
.phone{left:935px;top:20px;color:var(--yellow);font-weight:700;font-size:17px;display:flex;align-items:center;gap:10px}

/* hero */
.hero{left:0;top:60px;width:1200px;height:510px;background:linear-gradient(120deg,#1b3860,#0d1d36 55%,#24497a)}
.hero-title{left:142px;top:215px;color:var(--white);font-size:46px;font-weight:700}
.hero-text{left:144px;top:293px;color:var(--white);font-size:17px;line-height:31px;text-transform:uppercase;white-space:nowrap}
.btn{display:flex;align-items:center;justify-content:center;font-weight:600;text-transform:uppercase;color:var(--white)}
.hero-btn{left:142px;top:394px;width:152px;height:38px;background:var(--blue);font-size:16px}
.arrow{top:305px;width:24px;height:36px}

/* lead */
.lead-title{left:0;top:630px;width:1200px;text-align:center;color:var(--ink);font-size:48px;font-weight:700}
.lead-sub{left:0;top:698px;width:1200px;text-align:center;color:var(--blue);font-size:34px;font-weight:700}
.field{top:783px;width:328px;height:59px;background:var(--white);box-shadow:0 2px 8px rgba(0,0,0,.18);display:flex;align-items:center;justify-content:space-between;padding:0 26px;font-size:15px;color:#888}
.submit{left:887px;top:783px;width:121px;height:59px;background:var(--blue);font-size:16px;text-transform:none;font-weight:500}
.divider{left:0;top:922px;width:1200px;height:1px;background:#e5e5e5}

/* services */
.services-title{left:0;top:1006px;width:1200px;text-align:center;color:var(--blue);font-size:26px;font-weight:700}
.services-sub{left:0;top:1055px;width:1200px;text-align:center;color:var(--ink);font-size:25px;font-weight:700}
.card{width:452px;height:195px;background:var(--white);box-shadow:0 2px 12px rgba(0,0,0,.13);overflow:hidden}
.card-num{position:absolute;left:20px;top:12px;font-size:30px;font-weight:800;color:var(--grey-num)}
.card-num.warm{color:#f7c7a8}
.card-icon{position:absolute;left:25px;top:58px;width:100px;height:100px}
.card-title{position:absolute;left:162px;top:58px;font-size:18px;font-weight:600;color:var(--ink);white-space:nowrap}
.card-title.large{font-size:20px;top:56px}
.card-text{position:absolute;left:162px;top:92px;font-size:13px;line-height:26px;color:var(--text);white-space:nowrap}
.card-more{position:absolute;left:162px;top:155px;font-size:11px;color:var(--orange);text-transform:uppercase}
.card-corner{position:absolute;right:0;bottom:0;width:86px;height:86px;background:var(--blue);clip-path:polygon(100% 0,100% 100%,0 100%)}

/* seo */
.seo-band{left:0;top:1735px;width:1200px;height:600px;background:linear-gradient(90deg,#4a7cc9,#5382cc 60%,#6a93d2);clip-path:polygon(0 46px,727px 46px,773px 0,1200px 0,1200px 600px,0 600px)}
.seo-title{left:142px;top:1878px;color:var(--yellow);font-size:36px;font-weight:700}
.seo-text{left:144px;top:1962px;width:792px;color:var(--white);font-size:17px;line-height:31px;text-align:justify}
.seo-btn{left:143px;top:2142px;width:153px;height:40px;background:var(--yellow);font-size:16px;font-weight:500}

/* local */
.local-title{left:0;top:2434px;width:1200px;text-align:center;color:var(--blue);font-size:36px;font-weight:700}
.local-text{left:217px;top:2507px;width:766px;font-size:17px;line-height:32.5px;color:var(--ink);text-align:justify;text-align-last:center}
.local-btn{left:523px;top:2675px;width:153px;height:40px;background:var(--blue);font-size:16px;font-weight:500}

/* testimonials */
.testi-band{left:0;top:2803px;width:1200px;height:631px;background:var(--pale);clip-path:polygon(0 0,425px 0,470px 49px,1200px 49px,1200px 631px,0 631px)}
.quote{left:110px;top:2876px;width:50px;height:40px}
.photo-accent{left:292px;top:3125px;width:229px;height:225px;background:var(--yellow);clip-path:polygon(100% 0,100% 100%,0 100%,0 86%,86% 86%,86% 8%)}
.photo{left:112px;top:2943px;width:393px;height:390px;background:linear-gradient(160deg,#c9ccd1,#8d939b 60%,#5b6168)}
.testi-title{left:567px;top:2950px;color:var(--blue);font-size:42px;font-weight:700}
.testi-text{left:572px;top:3017px;font-size:15px;line-height:31px;color:var(--ink);white-space:nowrap;letter-spacing:-.1px}
.testi-name{left:572px;top:3236px;display:flex;align-items:baseline;gap:12px;color:var(--ink);white-space:nowrap}
.testi-name b{font-size:25px;font-weight:600}
.testi-name span{font-size:12px}
.testi-nav{left:608px;top:3320px;display:flex;align-items:center;gap:22px;color:var(--ink);font-size:20px}
.testi-nav i{display:block;width:3px;height:34px;background:var(--yellow)}

/* footer */
.footer{left:0;top:3434px;width:1200px;height:343px;background:var(--black)}
.connect{left:0;top:3478px;width:1200px;text-align:center;color:var(--yellow);font-size:44px;font-weight:300}
.connect-sub{left:0;top:3545px;width:1200px;text-align:center;color:var(--white);font-size:15px}
.news-input{left:321px;top:3592px;width:407px;height:64px;background:var(--blue);color:var(--white);font-size:14px;display:flex;align-items:center;padding-left:55px}
.news-btn{left:728px;top:3592px;width:141px;height:64px;background:var(--white);color:var(--black);font-size:17px;font-weight:500}
.social{left:477px;top:3679px;display:flex;gap:32px}
.social span{display:block;width:22px;height:22px;background:var(--white);border-radius:3px}
.copyright{left:0;top:3737px;width:1200px;text-align:center;color:var(--white);font-size:14px}
</style>
</head>
<body>

<!-- header -->
<div class="abs header"></div>
<div class="abs header-logo"></div>
<div class="abs brand">Velmorbix<small>Applications</small></div>
<nav class="abs nav">
  <a class="active" href="#">HOME</a>
  <a href="#">ABOUT US</a>
  <a href="#">SERVICES</a>
  <a href="#">BLOG</a>
  <a href="#">CONTACT</a>
</nav>
<div class="abs phone">
  <svg width="16" height="16" viewBox="0 0 16 16"><path d="M2 9a6 6 0 0 1 12 0" fill="none" stroke="#f6c624" stroke-width="2"/><rect x="1" y="8" width="4" height="6" rx="1" fill="#f6c624"/><rect x="11" y="8" width="4" height="6" rx="1" fill="#f6c624"/></svg>
  (555)-204-7718
</div>

<!-- hero -->
<div class="abs hero" role="img" aria-label="Hands holding a tablet surrounded by glowing digital marketing icons for email, video, mobile and website"></div>
<h1 class="abs hero-title">VELMORBIX</h1>
<p class="abs hero-text">Our mission is to empower every client with the web presence<br>that will drive them ahead of the competition.</p>
<div class="abs btn hero-btn">Get Started</div>
<svg class="abs arrow" style="left:58px" viewBox="0 0 24 36"><path d="M18 4 6 18l12 14" fill="none" stroke="#fff" stroke-width="4"/></svg>
<svg class="abs arrow" style="left:1110px" viewBox="0 0 24 36"><path d="M6 4l12 14L6 32" fill="none" stroke="#fff" stroke-width="4"/></svg>

<!-- lead form -->
<h2 class="abs lead-title">VELMORBIX</h2>
<p class="abs lead-sub">ARE YOU READY TO TAKE THE LEAD?</p>
<div class="abs field" style="left:192px">Enter your name
  <svg width="14" height="16" viewBox="0 0 14 16"><circle cx="7" cy="4.5" r="3.5" fill="#777"/><path d="M0 16c0-5 3-7 7-7s7 2 7 7z" fill="#777"/></svg>
</div>
<div class="abs field" style="left:540px">Enter your Email
  <svg width="18" height="13" viewBox="0 0 18 13"><rect width="18" height="13" rx="1" fill="#777"/><path d="M0 1l9 6 9-6" fill="none" stroke="#fff" stroke-width="1.4"/></svg>
</div>
<div class="abs btn submit">Submit</div>
<div class="abs divider"></div>

<!-- services -->
<h2 class="abs services-title">WEBSITE DESIGN, DEVELOPMENT &amp; HOSTING</h2>
<p class="abs services-sub">AND SEO CONSULTING</p>

<div class="abs card" style="left:120px;top:1177px">
  <span class="card-num">01</span>
  <svg class="card-icon" viewBox="0 0 100 100"><rect x="28" y="10" width="56" height="78" rx="4" fill="none" stroke="#4a7cc9" stroke-width="5"/><rect x="42" y="4" width="28" height="12" rx="3" fill="#4a7cc9"/><path d="M40 38h34M40 54h34M40 70h34" stroke="#4a7cc9" stroke-width="5"/><path d="M10 80l30-30" stroke="#2f5ea8" stroke-width="7"/><circle cx="28" cy="32" r="9" fill="none" stroke="#2f5ea8" stroke-width="4"/></svg>
  <h3 class="card-title">Web Writing Services</h3>
  <p class="card-text">Well-crafted web writing is a bal-<br>ancing act between message,</p>
  <span class="card-more">Learn More</span>
</div>

<div class="abs card" style="left:627px;top:1177px">
  <span class="card-num warm">02</span>
  <svg class="card-icon" viewBox="0 0 100 100"><path d="M10 72c15 0 25 12 45 8l30-12c4-2 2-8-3-7L58 68" fill="#4a7cc9"/><rect x="28" y="50" width="8" height="18" fill="#2f5ea8"/><rect x="42" y="40" width="8" height="28" fill="#2f5ea8"/><rect x="56" y="30" width="8" height="38" fill="#2f5ea8"/><rect x="70" y="22" width="8" height="46" fill="#2f5ea8"/><path d="M22 48l20-18 14 8 26-24" fill="none" stroke="#4a7cc9" stroke-width="5"/><path d="M74 10h12v12" fill="none" stroke="#4a7cc9" stroke-width="5"/></svg>
  <h3 class="card-title large">PPC</h3>
  <p class="card-text">Beyond organic SEO strategies,<br>Pay-Per-Click (PPC) tactics are one</p>
  <span class="card-more">Learn More</span>
  <div class="card-corner"></div>
</div>

<div class="abs card" style="left:120px;top:1435px">
  <span class="card-num">03</span>
  <svg class="card-icon" viewBox="0 0 100 100"><circle cx="42" cy="42" r="30" fill="none" stroke="#4a7cc9" stroke-width="7"/><path d="M64 64l22 22" stroke="#2f5ea8" stroke-width="12" stroke-linecap="round"/><rect x="38" y="24" width="8" height="24" rx="3" fill="#2f5ea8"/><circle cx="42" cy="58" r="5" fill="#2f5ea8"/></svg>
  <h3 class="card-title">Search Engine Optimization</h3>
  <p class="card-text">A website built with a strong SEO<br>base is essential. Powerful search</p>
  <span class="card-more">Learn More</span>
</div>

<div class="abs card" style="left:627px;top:1435px">
  <span class="card-num">04</span>
  <svg class="card-icon" viewBox="0 0 100 100"><path d="M40 10a40 40 0 0 0 0 80M60 90a40 40 0 0 0 0-80" fill="none" stroke="#4a7cc9" stroke-width="2" stroke-dasharray="4 4"/><circle cx="42" cy="50" r="13" fill="none" stroke="#2f5ea8" stroke-width="8" stroke-dasharray="5 3"/><circle cx="66" cy="36" r="8" fill="none" stroke="#4a7cc9" stroke-width="6" stroke-dasharray="4 2"/><circle cx="66" cy="66" r="8" fill="none" stroke="#4a7cc9" stroke-width="6" stroke-dasharray="4 2"/></svg>
  <h3 class="card-title large">Advanced Web Tools</h3>
  <p class="card-text">CRM or API integration, ecommerce ca-<br>pabilities, advanced calendars and</p>
  <span class="card-more">Learn More</span>
</div>

<!-- seo consulting -->
<div class="abs seo-band" role="img" aria-label="Blue-tinted photo of a laptop screen displaying digital marketing and social media graphics"></div>
<h2 class="abs seo-title">SEO CONSULTING</h2>
<p class="abs seo-text">As soon as possible. Recent studies show an increasing number of breast cancer cases in women under age 40 (when your first mammogram is recommended). You should begin using Thermal Imaging when you are 20 years old to establish a baseline—between ages 20 and 30, every 3 years, and annually after that.These recommendations</p>
<div class="abs btn seo-btn">Read More</div>

<!-- local optimization -->
<h2 class="abs local-title">LOCAL OPTIMIZATION</h2>
<p class="abs local-text">When online audiences can find businesses in their own backyard to answer all of their needs, your business can win—as long as your web strategy is prepared for these local queries.web strategy is prepared for these local queries.Beyond organic SEO strategies, Pay-Per-Click (PPC) tactics are one more way to get your business</p>
<div class="abs btn local-btn">Read More</div>

<!-- testimonials -->
<div class="abs testi-band"></div>
<svg class="abs quote" viewBox="0 0 50 40"><path d="M4 40V22C4 10 10 3 20 0l2 5c-6 3-8 7-8 12h8v23zM28 40V22c0-12 6-19 16-22l2 5c-6 3-8 7-8 12h8v23z" fill="#f6c624"/></svg>
<div class="abs photo-accent"></div>
<div class="abs photo" role="img" aria-label="Portrait photo of a smiling businessman in a suit with arms crossed"></div>
<h2 class="abs testi-title">TESTIMONIALS</h2>
<p class="abs testi-text">Lorieum prism informative, and available to answer any questions<br>during the exam, and as follow up after you receive your report. I will<br>most definitely be doing this in conjunction with my annual mam-<br>mogram! I didn't know quite what to expect when I showed up for<br>my Thermal Breast Imaging appointment at RVC. I was pleasantly<br>surprised to find the exam to be thorough</p>
<div class="abs testi-name"><b>Dr. Halvern</b><span>is respectful, conducts the imaging in a professional</span></div>
<div class="abs testi-nav"><span>&lsaquo;</span><i></i><span>&rsaquo;</span></div>

<!-- footer -->
<footer class="abs footer"></footer>
<h2 class="abs connect">LET'S CONNECT !</h2>
<p class="abs connect-sub">Lorem ipsum dolor sit amet, consectetur adipiscing elit,</p>
<div class="abs news-input">type your e-mail here</div>
<div class="abs btn news-btn">SUBMIT</div>
<div class="abs social"><span></span><span></span><span></span><span></span><span></span></div>
<p class="abs copyright">Copyright © 2020 velmorbix - All Rights Reserved.</p>

</body>
</html>
```